Spa Business Card Design Project

Hello! We are a boutique spa for men and women that is rebranding. I would like a memorable new business card that showcases our beautiful new logo and our unique business. I would like it to be classic/timeless and eclectic/artistic at the  same time.
I am a fan of negative space as you can tell from the logo. I am also open to any creative ideas.
Multi sided design. Two sided design is acceptable as an option, too. "Flaps/folds/whatever the design term is" are optional- whether full vertical or horizontal, half flap, full flap etc
On either side next to the golden snail I would potentially like to see "slow down. Enjoy Life."  Possibly on one statment on top of each other, crowned with the snail. Or the statment following the snail on one line... I am open for a creative suprise, too.
The back I would like room for the standard Information
"3187 Birch Lane
Halden, New York 12471
(518) 462 3058
info@thecorvale spa.com
The snail is to be done in gold ink.
Can I also Have an option for cards that are individualized for staff members, too?

Updates
Reason: I apologize for the deadline extension. My day was more involved than anticipated in other matters. Hope to have this closed by next Tuesday.
Thank you

Target Market(s)
Men and women with expendable income between the ages of 30-55
Industry/Entity Type
Boutique
Requirements
Must have
- only black and gold ink.

Nice to have
- One of a kind.
Showcase the snail :-)
make you smile :-)
Fun, but professional.
Should not have
- Lots of color.
Too feminine.
Too busy.

```html
<!DOCTYPE html>
<html lang="en">
<head>
<meta charset="utf-8">
<title>The Corvale Spa – Business Card</title>
<link rel="stylesheet" href="https://fonts.googleapis.com/css2?family=Cinzel:wght@500&family=Questrial&family=Delius&display=swap">
<style>
  :root {
    --backdrop: #e9e6e1;
    --card: #f6f6f4;
    --ink: #1d1d1d;
    --gold: #c7a75c;
    --gold-soft: #d4b773;
  }
  * { box-sizing: border-box; margin: 0; padding: 0; }
  html, body {
    width: 1200px;
    height: 880px;
    overflow: hidden;
    background: var(--backdrop);
  }
  .canvas {
    position: relative;
    width: 1200px;
    height: 880px;
  }
  .card {
    position: absolute;
    width: 600px;
    height: 343px;
    background: var(--card);
    box-shadow: 0 2px 6px rgba(0,0,0,0.12);
  }

  /* Front */
  .card-front { left: 70px; top: 470px; }
  .brand {
    position: absolute;
    left: 0; right: 0; top: 92px;
    text-align: center;
    font-family: "Cinzel", serif;
    font-weight: 500;
    color: var(--ink);
    font-size: 52px;
    line-height: 1.05;
    letter-spacing: 1px;
  }
  .brand-line { display: block; }
  .tagline {
    position: absolute;
    left: 0; right: 0; top: 236px;
    text-align: center;
    font-family: "Questrial", sans-serif;
    font-size: 19px;
    color: var(--ink);
    letter-spacing: 0.3px;
  }

  /* Back */
  .card-back { left: 530px; top: 70px; }
  .snail-art {
    position: absolute;
    left: 26px; top: 92px;
    width: 206px;
    height: 118px;
    background: var(--gold);
    border-radius: 70px 70px 14px 40px;
  }
  .bubble {
    position: absolute;
    left: 222px; top: 28px;
    width: 356px;
    height: 196px;
  }
  .contact {
    position: absolute;
    left: 292px; top: 52px;
    font-family: "Questrial", sans-serif;
    font-size: 18px;
    line-height: 1.55;
    color: var(--ink);
    list-style: none;
  }
  .slogan {
    position: absolute;
    right: 34px; top: 238px;
    font-family: "Delius", sans-serif;
    font-size: 33px;
    line-height: 1.15;
    color: var(--ink);
  }
  .slogan span { display: block; }
  .slogan .second { padding-left: 48px; }
</style>
</head>
<body>
<main class="canvas">

  <section class="card card-front" aria-label="Business card front">
    <h1 class="brand">
      <span class="brand-line">The</span>
      <span class="brand-line">Corvale Spa</span>
    </h1>
    <p class="tagline">a boutique spa for Men &amp; Women</p>
  </section>

  <section class="card card-back" aria-label="Business card back">
    <div class="snail-art" role="img" aria-label="Gold cartoon snail with a spiral shell, smiling"></div>
    <svg class="bubble" viewBox="0 0 356 196" aria-hidden="true">
      <path d="M52 0 H338 Q356 0 356 18 V178 Q356 196 338 196 H70 Q52 196 52 178 V120 L0 104 L52 88 V18 Q52 0 70 0 Z" fill="var(--gold-soft)"/>
    </svg>
    <ul class="contact">
      <li>3187 Birch Lane</li>
      <li>Halden, New York 12471</li>
      <li>(518) 462 3058</li>
      <li>info@thecorvale spa.com</li>
    </ul>
    <p class="slogan">
      <span>Slow Down.</span>
      <span class="second">Enjoy Life.</span>
    </p>
  </section>

</main>
</body>
</html>
```